A modern, fresh introduction to Buddhism

I need a book cover for an A6 sized book to be used both for ebook and hard copy. The author is a young, modern Buddhist teacher of high standing who has written this short intro to Buddhism in an informal Q & As format using modern, accessible language to convey profound and meaningful ideas to the general public. The author is Tibetan, but teaches worldwide and is very personable and dynamic. The cover should portray this and have a fresh yet authentic feel to it (nothing new-agey!). Please see the author's websites www.torvanelmiro.org and www.wbrt.org for reference, but do not feel that the design must align completely with the website designs.

Target Market(s)

General public both in Europe and America and in Asia ranging from teenagers to the elderly. A really broad audience.

Industry/Entity Type

Teacher

Requirements
Must have
• Please include the following text that on the front cover:

A Breath of Quiet Rivers

By Venerable Tsomar Deleng

Please include the following on the back cover:

Yarkun Tselpa Publications (with attached logo above it)
Nice to have
• A simplistic, artistic, and modern look without any traditional religious images.
Should not have
• No buddha images or religious images. I would prefer a more simplistic, modern and artistic look.

```html
<!DOCTYPE html>
<html lang="en">
<head>
<meta charset="utf-8">
<title>A Breath of Quiet Rivers — Book Cover</title>
<link rel="stylesheet" href="https://fonts.googleapis.com/css2?family=Oswald:wght@500;700&family=Noto+Serif:wght@700&display=swap">
<style>
  :root {
    --stage: #e9e9ea;
    --cover-back: #d4d4d6;
    --cover-front: #e4e4e6;
    --ink: #111111;
    --ink-soft: #1d1d1d;
    --box: #1a1a1a;
    --box-text: #a3a3a3;
    --sky-deep: #1f5fb4;
    --sky-mid: #5c97d6;
    --sky-light: #b9d3ec;
    --mist: #e4e4e6;
  }
  * { margin: 0; padding: 0; box-sizing: border-box; }
  html, body { width: 1200px; height: 800px; overflow: hidden; }
  body {
    background: var(--stage);
    position: relative;
    font-family: "Oswald", "Arial Narrow", sans-serif;
    color: var(--ink);
  }
  .cover {
    position: absolute;
    top: 120px;
    width: 390px;
    height: 556px;
    overflow: hidden;
    box-shadow: 0 6px 24px rgba(0,0,0,0.12);
  }
  /* Back cover */
  .cover--back {
    left: 150px;
    background: var(--cover-back);
    padding: 10px 26px 0;
    text-align: center;
  }
  .back-author {
    font-size: 9px;
    font-weight: 700;
    letter-spacing: 0.2px;
  }
  .back-title {
    font-size: 42px;
    font-weight: 700;
    line-height: 0.98;
    text-transform: uppercase;
    margin-top: 2px;
  }
  .back-subtitle {
    font-size: 12.5px;
    font-weight: 700;
    text-transform: uppercase;
    margin-top: 2px;
  }
  .back-blurb {
    font-family: "Noto Serif", Georgia, serif;
    font-weight: 700;
    font-size: 9.2px;
    line-height: 1.36;
    text-align: justify;
    text-align-last: center;
    color: var(--ink-soft);
    margin-top: 4px;
    height: 318px;
    overflow: hidden;
  }
  .back-marks {
    position: absolute;
    left: 26px;
    right: 26px;
    bottom: 12px;
    display: flex;
    justify-content: space-between;
  }
  .mark-box {
    width: 110px;
    height: 58px;
    padding: 0 10px;
    background: var(--box);
    color: var(--box-text);
    font-family: "Noto Serif", Georgia, serif;
    font-size: 10px;
    display: flex;
    align-items: center;
    justify-content: center;
    text-align: center;
  }
  .mark-box--publisher {
    font-family: "Oswald", "Arial Narrow", sans-serif;
    font-weight: 500;
    font-size: 11px;
    line-height: 1.25;
    text-transform: uppercase;
    letter-spacing: 0.3px;
  }
  /* Front cover */
  .cover--front {
    left: 660px;
    background: var(--cover-front);
    text-align: center;
  }
  .front-art {
    position: absolute;
    left: 0; top: 0;
    width: 100%;
    height: 350px;
    background: linear-gradient(180deg, var(--sky-deep) 0%, var(--sky-mid) 28%, var(--sky-light) 62%, var(--mist) 100%);
  }
  .front-text {
    position: absolute;
    left: 0; right: 0;
    top: 356px;
  }
  .front-title {
    font-size: 52px;
    font-weight: 700;
    line-height: 1.0;
    text-transform: uppercase;
    text-shadow: 1px 2px 2px rgba(0,0,0,0.25);
  }
  .front-subtitle {
    font-size: 14.5px;
    font-weight: 700;
    text-transform: uppercase;
    margin-top: 4px;
  }
  .front-author {
    font-size: 11px;
    font-weight: 700;
    margin-top: 26px;
  }
</style>
</head>
<body>
  <section class="cover cover--back" aria-label="Back cover">
    <p class="back-author">Venerable Tsomar Deleng</p>
    <h2 class="back-title">A Breath of<br>Quiet Rivers</h2>
    <p class="back-subtitle">A short introduction to the Buddha's teaching</p>
    <p class="back-blurb">Lorem ipsum dolor sit amet, consectetur adipisicing elit, sed do eiusmod tempor incididunt ut labore et dolore magna aliqua. Ut enim ad minim veniam, quis nostrud exercitation. Lorem ipsum dolor sit amet, consectetur adipisicing elit, sed do eiusmod tempor incididunt ut labore et dolore magna aliqua. Ut enim ad minim veniam, quis nostrud exercitation. Lorem ipsum dolor sit amet, consectetur adipisicing elit, sed do eiusmod tempor incididunt ut labore et dolore magna aliqua. Ut enim ad minim veniam, quis nostrud exercitation. Lorem ipsum dolor sit amet, consectetur adipisicing elit, sed do eiusmod tempor incididunt ut labore et dolore magna aliqua. Ut enim ad minim veniam, quis nostrud exercitation. Lorem ipsum dolor sit amet, consectetur adipisicing elit, sed do eiusmod tempor incididunt ut labore et dolore magna aliqua. Ut enim ad minim veniam, quis nostrud exercitation. Lorem ipsum dolor sit amet, consectetur adipisicing elit, sed do eiusmod tempor incididunt ut labore et dolore magna aliqua. Ut enim ad minim veniam, quis nostrud exercitation. Lorem ipsum dolor sit amet, consectetur adipisicing elit, sed do eiusmod tempor incididunt ut labore et dolore magna aliqua. Ut enim ad minim veniam, quis nostrud exercitation. Lorem ipsum dolor sit amet, consectetur adipisicing elit, sed do eiusmod tempor incididunt ut labore et dolore magna aliqua. Ut enim ad minim veniam, quis nostrud exercitation. Lorem ipsum dolor sit amet, consectetur adipisicing elit, sed do eiusmod tempor incididunt ut labore et dolore magna aliqua. Ut enim ad minim veniam, quis nostrud exercitation.</p>
    <div class="back-marks">
      <div class="mark-box mark-box--isbn">ISBN</div>
      <div class="mark-box mark-box--publisher">Yarkun Tselpa Publications</div>
    </div>
  </section>

  <section class="cover cover--front" aria-label="Front cover">
    <div class="front-art" role="img" aria-label="Blue sky with white clouds above a seated stone statue and smooth black pebbles"></div>
    <div class="front-text">
      <h1 class="front-title">A Breath of<br>Quiet Rivers</h1>
      <p class="front-subtitle">A short introduction to the Buddha's teaching</p>
      <p class="front-author">Venerable Tsomar Deleng</p>
    </div>
  </section>
</body>
</html>
```